Business Card Design Project

The overall design must be suitable alongside our company logo which is attached

There must be space for the agent to write their name & telephone number

Card must contain the words:

Maple Carpet Cleaning

Agent:
Tel:

Target Market(s)

Industry/Entity Type

Business

```html
<!DOCTYPE html>
<html lang="en">
<head>
<meta charset="utf-8">
<title>Maple Carpet Cleaning – Business Card</title>
<link href="https://fonts.googleapis.com/css2?family=Mulish:wght@500;600&display=swap" rel="stylesheet">
<style>
  :root {
    --ink: #231f1a;
    --gold: #b5924a;
    --paper: #ffffff;
    --edge: #8c8c8c;
  }
  html, body {
    margin: 0;
    padding: 0;
    overflow: hidden;
    background: var(--paper);
  }
  .canvas {
    position: relative;
    width: 1050px;
    height: 1200px;
    background: var(--paper);
    font-family: "Mulish", Arial, sans-serif;
    color: var(--ink);
    overflow: hidden;
  }

  /* Front face */
  .card-front {
    position: absolute;
    left: 0; top: 0;
    width: 1050px; height: 598px;
  }
  .front-brand {
    position: absolute;
    left: 230px; top: 250px;
    width: 590px;
    display: flex;
    align-items: center;
    gap: 24px;
  }
  .brand-dot {
    flex: none;
    width: 64px; height: 64px;
    border-radius: 50%;
    background: var(--gold);
  }
  .brand-name {
    font-weight: 600;
    color: var(--ink);
    white-space: nowrap;
    line-height: 1;
  }
  .front-brand .brand-name { font-size: 50px; }
  .front-rule {
    position: absolute;
    left: 463px; top: 368px;
    width: 312px; height: 9px;
    border-top: 3px solid var(--ink);
    border-bottom: 3px solid var(--ink);
    box-sizing: border-box;
  }

  /* Back face */
  .card-back {
    position: absolute;
    left: -2px; top: 599px;
    width: 1050px; height: 599px;
    border: 2px solid var(--edge);
    border-left: none;
    box-sizing: content-box;
  }
  .back-brand {
    position: absolute;
    left: 102px; top: 100px;
    font-size: 58px;
  }
  .back-rule {
    position: absolute;
    left: 0; top: 171px;
    width: 1050px; height: 9px;
    border-top: 3px solid var(--ink);
    border-bottom: 3px solid var(--ink);
    box-sizing: border-box;
  }
  .write-field {
    position: absolute;
    left: 102px;
    display: flex;
    align-items: baseline;
    font-size: 36px;
    font-weight: 500;
    letter-spacing: -0.5px;
  }
  .write-field .field-line {
    display: block;
    height: 4px;
    background: var(--ink);
    align-self: flex-end;
    margin-bottom: 2px;
  }
  .field-agent { top: 297px; }
  .field-agent .field-line { width: 687px; margin-left: 36px; }
  .field-tel { top: 412px; }
  .field-tel .field-line { width: 523px; margin-left: 78px; }

  .back-mark {
    position: absolute;
    left: 790px; top: 430px;
    display: flex;
    align-items: center;
    gap: 12px;
  }
  .back-mark .brand-dot { width: 28px; height: 28px; }
  .back-mark .brand-name { font-size: 20px; }
</style>
</head>
<body>
<div class="canvas">

  <section class="card-front" aria-label="Card front">
    <div class="front-brand">
      <span class="brand-dot"></span>
      <span class="brand-name">Maple Carpet Cleaning</span>
    </div>
    <div class="front-rule"></div>
  </section>

  <section class="card-back" aria-label="Card back">
    <div class="brand-name back-brand">Maple Carpet Cleaning</div>
    <div class="back-rule"></div>

    <div class="write-field field-agent">
      <span class="field-label">Agent:</span>
      <span class="field-line"></span>
    </div>
    <div class="write-field field-tel">
      <span class="field-label">Tel:</span>
      <span class="field-line"></span>
    </div>

    <div class="back-mark">
      <span class="brand-dot"></span>
      <span class="brand-name">Maple Carpet<br>Cleaning</span>
    </div>
  </section>

</div>
</body>
</html>
```